Tidewell Gin - Label for new Gin bottle

I am looking for a bottle label for our small batch, handcrafted Gin. We are located in the bay-side city of Frankston (Victoria, Australia). I know I want more of a serious label but am torn between traditional or modern styling.

Label to include;
• Tidewell GIN (name)
• Hand Crafted
• Small Batch
• 40% Vol

Using 700ml MERIDA Spirit Bottle - Cork

Requirements
Must have
• Name; Tidewell Gin
Method: Hand Crafted
Batch Size; Small Batch
Alc; 40% Vol
Nice to have
• Maybe a coastal/seaside reference or reference to distilling.

```html
<!DOCTYPE html>
<html lang="en">
<head>
<meta charset="utf-8">
<title>Tidewell Gin – Bottle Label</title>
<link rel="stylesheet" href="https://fonts.googleapis.com/css2?family=Quicksand:wght@400;500;700&display=swap">
<style>
  :root {
    --page-bg: #ffffff;
    --label-bg: #000000;
    --brand-name: #d3c0dc;
    --accent-purple: #8c4f9e;
    --text-white: #ffffff;
    --text-grey: #b5b5b5;
  }
  html, body {
    margin: 0;
    padding: 0;
    width: 1200px;
    height: 1200px;
    overflow: hidden;
    background: var(--page-bg);
  }
  .canvas {
    position: relative;
    width: 1200px;
    height: 1200px;
  }
  .gin-label {
    position: absolute;
    left: 361px;
    top: 60px;
    width: 478px;
    height: 1080px;
    display: block;
  }
  .gin-label text {
    font-family: "Quicksand", sans-serif;
  }
  .label-ground { fill: var(--label-bg); }
  .method { fill: var(--accent-purple); font-size: 24px; font-weight: 500; letter-spacing: 0.5px; }
  .brand-name { fill: var(--brand-name); font-weight: 700; }
  .brand-first { font-size: 96px; }
  .brand-second { font-size: 330px; }
  .batch { fill: var(--text-white); font-size: 22px; font-weight: 500; }
  .volume { fill: var(--accent-purple); font-size: 36px; font-weight: 500; }
  .strength { fill: var(--text-grey); font-size: 22px; font-weight: 400; }
  .origin { fill: var(--accent-purple); font-size: 16px; font-weight: 500; }
</style>
</head>
<body>
<main class="canvas">
  <svg class="gin-label" viewBox="0 0 478 1080" xmlns="http://www.w3.org/2000/svg" aria-label="Tidewell Gin bottle label">
    <rect class="label-ground" x="0" y="0" width="478" height="1080"/>

    <text class="method" x="425" y="296" text-anchor="end">HAND CRAFTED</text>

    <text class="brand-name brand-first" x="48" y="373" textLength="380" lengthAdjust="spacingAndGlyphs">Tidewell</text>
    <text class="brand-name brand-second" x="48" y="641" textLength="378" lengthAdjust="spacingAndGlyphs">Gin</text>

    <text class="batch" x="270" y="763">Small Batch</text>
    <text class="volume" x="98" y="864">700ml</text>

    <text class="strength" x="239" y="1012" text-anchor="middle">40% Vol</text>
    <text class="origin" x="239" y="1053" text-anchor="middle">Harlow Bay, Australia</text>
  </svg>
</main>
</body>
</html>
```